Heating and Air Conditioning Company Needs a Business Card Design

Need a business card design for a company in South Carolina called "Larkfield Heating & Cooling LLC". We install, maintain, and repair HVAC systems and the bulk of our business is residential. We have a logo and are looking for a clean, professional looking card that resonates with "setting the standard for service and comfort".
Updates
Forgot to include this info - Licensed & Insured

Industry/Entity Type
Business

```html
<!DOCTYPE html>
<html lang="en">
<head>
<meta charset="utf-8">
<title>Larkfield Heating &amp; Cooling LLC — Business Card</title>
<link rel="stylesheet" href="https://fonts.googleapis.com/css2?family=Tinos:wght@400;700&display=swap">
<style>
  :root {
    --page-bg: #e9e6e1;
    --card-white: #ffffff;
    --brand-blue: #0b4ea2;
    --accent-blue: #1b7fd1;
    --brand-red: #e31e26;
    --brand-orange: #f5a01a;
    --plumb-grey: #7d7d7d;
    --ink: #111111;
    --rule: #c9c9c9;
  }
  * { margin: 0; padding: 0; box-sizing: border-box; }
  html, body {
    width: 1200px; height: 750px; overflow: hidden;
    background: var(--page-bg);
    font-family: "Tinos", "Times New Roman", serif;
    color: var(--ink);
  }
  .card {
    position: absolute; left: 120px; top: 70px;
    width: 960px; height: 610px;
    background: var(--card-white);
    box-shadow: 0 10px 30px rgba(0,0,0,.25);
    overflow: hidden;
  }
  .card-shapes { position: absolute; inset: 0; }
  .brand {
    position: absolute; left: 0; width: 900px; top: 112px;
    display: flex; justify-content: center; align-items: center; gap: 16px;
  }
  .brand-dot {
    width: 34px; height: 34px; border-radius: 50%;
    background: var(--brand-blue);
  }
  .brand-name {
    font-weight: 700; font-size: 44px; color: var(--brand-blue);
    letter-spacing: .5px; white-space: nowrap;
  }
  .person { position: absolute; left: 116px; top: 236px; }
  .person-name { font-weight: 700; font-size: 28px; }
  .person-title { font-size: 18px; color: var(--accent-blue); margin-top: 2px; }
  .address { font-size: 17px; line-height: 22px; margin-top: 22px; }
  .email { font-size: 21px; margin-top: 20px; }
  .divider {
    position: absolute; left: 496px; top: 215px;
    width: 2px; height: 200px; background: var(--rule);
  }
  .phones { position: absolute; left: 568px; top: 238px; list-style: none; }
  .phones li { font-weight: 700; font-size: 23px; height: 65px; }
  .services {
    position: absolute; left: 0; width: 956px; top: 420px;
    text-align: center; font-weight: 700;
  }
  .services-types { font-size: 23px; }
  .svc-heat { color: var(--brand-red); }
  .svc-cool { color: var(--brand-blue); }
  .svc-plumb { color: var(--plumb-grey); }
  .services-sectors { font-size: 23px; margin-top: 8px; }
  .website { font-size: 21px; letter-spacing: 4px; margin-top: 10px; }
</style>
</head>
<body>
  <main class="card">
    <svg class="card-shapes" width="960" height="610" viewBox="0 0 960 610" aria-hidden="true">
      <path d="M864 0 H960 V610 H775 C880 470 905 250 864 0 Z" fill="var(--brand-blue)"/>
      <rect x="0" y="540" width="425" height="70" fill="var(--brand-orange)"/>
      <path d="M429 610 V552 Q429 540 441 540 H828 Q840 540 832 552 Q820 580 792 610 Z" fill="var(--brand-red)"/>
    </svg>

    <div class="brand">
      <span class="brand-dot"></span>
      <span class="brand-name">Larkfield Heating &amp; Cooling LLC</span>
    </div>

    <section class="person">
      <h1 class="person-name">Dale Hartwell</h1>
      <p class="person-title">Certified Technician</p>
      <p class="address">245 Mill Creek Lane,<br>Greenwood, SC 29646</p>
      <p class="email">dale@larkfieldhc.net</p>
    </section>

    <div class="divider"></div>

    <ul class="phones">
      <li>Tel – (864) 555-0142</li>
      <li>Fax – (864) 555-0187</li>
      <li>Cell – (864) 555-0163</li>
    </ul>

    <section class="services">
      <p class="services-types"><span class="svc-heat">Heating</span> • <span class="svc-cool">Cooling</span> • <span class="svc-plumb">Plumbing</span></p>
      <p class="services-sectors">Residential • Commercial • Industrial</p>
      <p class="website">www.larkfieldhc.net</p>
    </section>
  </main>
</body>
</html>
```